Web3.0 Metaverse as a Service Pitch Deck

We need our investor pitch deck to look slick and professional. It should be easy to read/view with large text (investors see hundreds of these a week).
https://www.tallowbridge.example/library/4T-how-to-design-a-better-pitch-deck
Just the first 10 slides, two of which should be combined (monetization):
https://links.quintrapex.example/pitchdeckwip

```html
<!DOCTYPE html>
<html lang="en">
<head>
<meta charset="utf-8">
<title>Quintrapex — Metaverse-as-a-Service Pitch Deck</title>
<link href="https://fonts.googleapis.com/css2?family=Montserrat:wght@300;400;600;700&family=Rubik:wght@700;800&display=swap" rel="stylesheet">
<style>
  :root{
    --teal:#2fe0b4;
    --teal-deep:#1f9f86;
    --purple:#8a14d8;
    --ink:#000;
    --paper:#e9e9ef;
    --muted:#8d8d99;
    --space-top:#1c1326;
    --space-mid:#2a1640;
    --space-violet:#4a1a6e;
    --space-blue:#243a6a;
    --head:"Rubik",sans-serif;
    --body:"Montserrat",sans-serif;
  }
  *{box-sizing:border-box;margin:0;padding:0}
  html,body{width:767px;height:1200px;overflow:hidden}
  body{
    position:relative;font-family:var(--body);color:var(--paper);
    background:
      radial-gradient(ellipse 420px 380px at 0% 60%,var(--space-violet) 0%,transparent 70%),
      radial-gradient(ellipse 380px 420px at 100% 78%,var(--space-blue) 0%,transparent 70%),
      radial-gradient(ellipse 500px 300px at 60% 100%,var(--space-violet) 0%,transparent 75%),
      linear-gradient(180deg,var(--space-top) 0%,var(--space-mid) 55%,#2b1248 100%);
  }
  .starfield{position:absolute;inset:0}
  .slide{position:absolute;width:320px;height:180px;background:var(--ink);overflow:hidden}
  .slide *{position:absolute}
  .s-title{left:50px;top:75px}
  .s-team{left:400px;top:75px}
  .s-problem{left:50px;top:292px}
  .s-solution{left:400px;top:292px}
  .s-value{left:50px;top:509px}
  .s-money{left:400px;top:509px}
  .s-traction{left:50px;top:726px}
  .s-plan{left:400px;top:726px}
  .s-close{left:223px;top:942px}

  .wordmark{left:0;right:0;top:80px;text-align:center;font-weight:300;font-size:14px;letter-spacing:5px;color:var(--teal)}

  .heading{font-family:var(--head);font-weight:800;color:var(--teal);line-height:1}
  .small{font-size:3.6px;line-height:5px;color:var(--paper)}

  /* team */
  .avatar{width:35px;height:35px;border-radius:50%;left:23px;border:2px solid var(--teal-deep);background:#4b3a9a}
  .bio{left:76px;width:176px}
  .bio b,.bio span{position:static}
  .team-title{left:256px;top:20px;font-size:20px}
  .badges{left:98px;top:155px;display:flex;gap:9px;align-items:center}
  .badges span{position:static;display:block;width:11px;height:8px;background:#6d6d78;border-radius:2px}
  .badges span.round{width:9px;height:9px;border-radius:50%}

  /* problem */
  .problem-sky{inset:0;background:radial-gradient(ellipse 220px 120px at 40% 40%,#0d1a17,#000 80%)}
  .problem-title{left:22px;top:20px;font-size:16px}
  .ringed-art{left:62px;top:42px;width:72px;height:64px;background:linear-gradient(150deg,#2a2518,#6e6040 55%,#1a1710)}
  .planets-art{left:204px;top:48px;width:84px;height:84px;background:linear-gradient(135deg,#5a4a2c,#2c4a5c 50%,#5a3a24)}
  .problem-copy{left:20px;width:150px;top:106px;text-align:center;font-size:3.6px;line-height:5px;color:var(--paper)}
  .terrain{left:0;bottom:0;width:320px;height:34px;background:linear-gradient(180deg,transparent 0%,#1a3a9a 45%,#3f6fe0 70%,#b0344f 100%)}

  /* solution */
  .solution-art{left:150px;top:0;width:170px;height:180px;background:linear-gradient(200deg,#6a5a4a,#2c2a45 55%,#0a0a18 100%)}
  .solution-title{left:13px;top:16px;font-size:23px}
  .solution-sub{left:13px;top:42px;font-family:var(--head);font-weight:800;font-size:9px;color:var(--purple)}
  .solution-copy{left:13px;top:86px;width:180px;font-size:3.6px;line-height:5px;color:var(--teal)}
  .solution-copy p,.solution-copy ul,.solution-copy li{position:static}
  .solution-copy li{list-style:none;padding-left:6px}

  /* value */
  .icon{width:13px;height:13px}
  .v-label{font-size:3.8px;color:var(--paper)}
  .v-text{font-size:3.6px;line-height:5px;color:var(--paper);width:82px}
  .value-word{left:212px;top:120px;width:86px;height:27px}
  .value-band{left:0;bottom:0;width:86px;height:13px;background:var(--purple)}
  .value-word b{left:0;top:-1px;width:86px;text-align:center;font-family:var(--head);font-weight:800;font-size:23px;color:var(--teal);line-height:1}

  /* monetization */
  .money-title{left:35px;top:32px;font-size:6.4px}
  .money-sign{left:50px;top:48px;font-family:var(--head);font-weight:800;font-size:42px;color:var(--teal);line-height:1}
  .money-notes{left:36px;top:110px;font-size:3.6px;line-height:6.2px;color:var(--paper)}
  .m-block{left:118px;width:120px}
  .m-head{font-size:3.9px;font-weight:700;color:var(--teal);position:static}
  .m-text{font-size:3.6px;line-height:7px;color:var(--paper);position:static}
  .m-text span{position:static;color:var(--teal)}
  .money-bar{left:312px;top:65px;width:8px;height:115px;background:var(--purple)}

  /* traction */
  .city{inset:0;background:radial-gradient(ellipse 200px 120px at 60% 20%,#3a1c66,transparent 70%),linear-gradient(180deg,#140a24 0%,#2a1350 60%,#43206e 100%)}
  .traction-copy{left:26px;top:23px;font-size:3.8px;line-height:7px;color:var(--paper)}
  .traction-title{left:210px;top:20px;font-size:16px}
  .shot{width:65px;height:39px}
  .shot::before{content:"";position:absolute;left:3px;top:3px;width:65px;height:39px;background:var(--teal)}
  .shot i{position:absolute;inset:0;border:2px solid var(--purple)}

  /* plan */
  .plan-title{left:23px;top:26px;font-size:18px;line-height:22px}
  .pie{left:36px;top:70px;width:100px;height:80px}
  .plan-band{left:176px;top:29px;width:144px;height:5px;background:var(--purple)}
  .plan-funding{left:176px;top:42px;font-family:var(--head);font-weight:700;font-size:8px;color:var(--teal)}
  .plan-copy{left:176px;top:58px;width:128px;font-size:3.6px;line-height:7px;color:var(--paper)}
  .plan-item{left:176px;font-size:3.6px;line-height:5px;color:var(--paper)}
  .plan-item b{position:static;display:block;color:var(--teal);font-weight:700}

  /* close */
  .close-copy{left:0;right:0;text-align:center;font-size:3.8px;line-height:7px;color:var(--teal)}
  .socials{left:0;right:0;top:143px;display:flex;justify-content:center;gap:10px}
  .socials span{position:static;font-size:4px;font-weight:600;color:var(--muted)}
</style>
</head>
<body>

<svg class="starfield" width="767" height="1200" aria-hidden="true">
  <g fill="#e9e6f5">
    <circle cx="76" cy="32" r="2"/><circle cx="242" cy="35" r="1.4"/><circle cx="378" cy="27" r="1.2"/><circle cx="468" cy="30" r="1.6"/><circle cx="614" cy="25" r="1.4"/><circle cx="700" cy="37" r="1.4"/><circle cx="735" cy="72" r="1.2"/>
    <circle cx="20" cy="110" r="1.3"/><circle cx="382" cy="103" r="1.5"/><circle cx="746" cy="180" r="1.4"/><circle cx="25" cy="230" r="1.4"/><circle cx="380" cy="262" r="1.2"/>
    <circle cx="742" cy="305" r="1.3"/><circle cx="375" cy="440" r="1.2"/><circle cx="28" cy="380" r="1.4"/><circle cx="744" cy="480" r="1.2"/><circle cx="412" cy="490" r="1.5"/>
    <circle cx="30" cy="560" r="1.3"/><circle cx="380" cy="600" r="1.4"/><circle cx="746" cy="640" r="1.2"/><circle cx="36" cy="720" r="1.2"/><circle cx="420" cy="700" r="1.2"/>
    <circle cx="380" cy="790" r="1.5"/><circle cx="760" cy="790" r="1.2"/><circle cx="320" cy="932" r="2.4"/><circle cx="690" cy="1040" r="3"/>
    <circle cx="60" cy="950" r="1.4"/><circle cx="150" cy="1000" r="1.2"/><circle cx="110" cy="1080" r="1.4"/><circle cx="600" cy="980" r="1.3"/><circle cx="640" cy="1120" r="1.4"/>
    <circle cx="408" cy="1180" r="3"/><circle cx="300" cy="1150" r="1.2"/><circle cx="520" cy="1160" r="1.4"/><circle cx="40" cy="1170" r="1.2"/><circle cx="720" cy="1180" r="1.3"/>
  </g>
  <g stroke="#e9e6f5" stroke-width="0.6" opacity="0.8">
    <path d="M242 20v30M228 35h28"/><path d="M396 918v28M382 932h28"/>
  </g>
</svg>

<!-- Cover -->
<section class="slide s-title">
  <p class="wordmark">QUINTRAPEX</p>
</section>

<!-- Core team -->
<section class="slide s-team">
  <div class="avatar" role="img" aria-label="Illustrated portrait of Dorian Vale" style="top:20px"></div>
  <div class="avatar" role="img" aria-label="Illustrated portrait of Rowan Hart" style="top:64px"></div>
  <div class="avatar" role="img" aria-label="Illustrated portrait of Emil Sarno" style="top:109px"></div>

  <div class="bio small" style="top:20px">
    <b style="font-weight:700">Dorian Vale</b><br>Co-Founder, Platform Lead<br><span style="display:block;height:3px"></span>
    Industry leader in Extended Reality (XR) development with &gt;10 years experience. Deployed over a half dozen multiplayer (&gt;1000 concurrent users) game engines for Global 500 clients. Expertise leading product development teams for immersive experiences. Startup veteran with dozens of XR products developed and shipped.
  </div>
  <div class="bio small" style="top:64px">
    <b style="font-weight:700">Rowan Hart</b><br>Co-Founder,<br>Development Lead<br><span style="display:block;height:3px"></span>
    Seasoned developer with 20+ year background building products &amp; businesses. Former CTO for VC-backed cloud-integrated payment platform and mentor for Kestrel Foundation's Innovation Corps. Directed the Ardenfield Startup Accelerator, LaunchKiln. Experience advising tech &amp; crypto ventures since 2013.
  </div>
  <div class="bio small" style="top:109px">
    <b style="font-weight:700">Emil Sarno</b><br>Design Lead<br><span style="display:block;height:3px"></span>
    Multi-engine game virtuoso with 20+ year track record curating 3D artistic vision on-the-fly. Streamvale Partner pioneering one of the most independently customized &amp; interactive horror gaming channels on the platform. Marketing-adept videographer with unparalleled attention to detail.
  </div>

  <h2 class="heading team-title">Core<br>Team</h2>

  <div class="badges" aria-label="Past partners">
    <span class="round"></span><span></span><span></span><span class="round"></span><span></span><span></span><span></span><span class="round"></span><span></span><span></span>
  </div>
</section>

<!-- Problem -->
<section class="slide s-problem">
  <div class="problem-sky"></div>
  <h2 class="heading problem-title">The Problem</h2>
  <div class="ringed-art" role="img" aria-label="Illustration of a ringed planet in deep space"></div>
  <p class="problem-copy">The majority of web3 projects include the word 'metaverse' on their roadmap. For 99% of them, this is marketing jargon that actualizes into a simplistic 3D 'game'.<br><br>Disparate, project-exclusive 3D games offer a poor (limited, boring) UX and require a very skilled team to build, deploy, and maintain.</p>
  <svg style="left:170px;top:88px" width="12" height="12" aria-hidden="true"><circle cx="6" cy="6" r="5.4" fill="none" stroke="#9a9aa6" stroke-width="0.6"/><path d="M5 3.5 7.5 6 5 8.5" fill="none" stroke="#9a9aa6" stroke-width="0.6"/></svg>
  <div class="planets-art" role="img" aria-label="Illustration of four separate planets, one per quadrant"></div>
  <svg style="left:202px;top:46px" width="88" height="88" aria-hidden="true"><path d="M44 0v88M0 44h88" stroke="var(--teal)" stroke-width="0.8"/></svg>
  <div class="terrain" role="img" aria-label="Neon wireframe mountain landscape"></div>
</section>

<!-- Solution -->
<section class="slide s-solution">
  <div class="solution-art" role="img" aria-label="Planets and ringed worlds across a starry sky"></div>
  <h2 class="heading solution-title">SOLUTION</h2>
  <p class="solution-sub">METAVERSE-AS-A-SERVICE</p>
  <div class="solution-copy">
    <p>Quintrapex offers a one-stop 'launch-into-the-metaverse' platform.<br>Partners (companies, brands, and communities) and individuals can purchase and design their own 3D experience with 0 coding or infrastructure. Core services include:</p>
    <ul style="margin-top:4px">
      <li>-&nbsp; No-code world building &amp; asset import GUI to create + launch a completely unique 3D space (ranging from a single structure to entire world)</li>
      <li>-&nbsp; Platform-wide marketplace for digital sales, subscriptions, and services</li>
      <li>-&nbsp; In-game economic layer for exclusivity, access, or leasing</li>
      <li>-&nbsp; Premium (variable cost) in-house 3D assets &amp; customization</li>
    </ul>
  </div>
</section>

<!-- Value -->
<section class="slide s-value">
  <svg class="icon" style="left:29px;top:43px" viewBox="0 0 13 13" aria-hidden="true"><g fill="none" stroke="var(--teal)" stroke-width="1"><path d="M2 4h9l-.5 8h-8z"/><path d="M4.5 4V3a2 2 0 0 1 4 0v1"/><path d="M4.5 7a2 2 0 0 0 4 0"/></g></svg>
  <p class="v-label" style="left:55px;top:41px">In-Game Transactions</p>
  <p class="v-text" style="left:55px;top:50px">Brands can embed B2C Shops in the metaverse, 2.5% fee</p>

  <p class="heading" style="left:30px;top:77px;font-size:17px">$</p>
  <p class="v-label" style="left:55px;top:76px">No Development Costs</p>
  <p class="v-text" style="left:55px;top:85px">Remove the development barrier for digitizing brands and rewarding customers with digital collectibles.</p>

  <svg class="icon" style="left:29px;top:119px" viewBox="0 0 13 13" aria-hidden="true"><g fill="none" stroke="var(--teal)" stroke-width="1"><rect x="2.5" y="2" width="8" height="10" rx="1"/><path d="M5 1.5h3v1.5H5z"/><path d="M4.5 7.5 6 9l3-3"/></g></svg>
  <p class="v-label" style="left:55px;top:116px">Pre-Built Feature Selection</p>
  <p class="v-text" style="left:55px;top:125px">Create experiences with drag and drop tools that require no coding experience.</p>

  <svg class="icon" style="left:185px;top:44px" viewBox="0 0 13 13" aria-hidden="true"><g fill="var(--teal)"><path d="M1 2h11l-1.5 2H1z"/><path d="M2.5 5.5h9.5L10.5 7.5H1z"/><path d="M1 9h11l-1.5 2H1z"/></g></svg>
  <p class="v-label" style="left:217px;top:41px">Extended Services</p>
  <p class="v-text" style="left:217px;top:50px;width:90px">A la carté services and content creation — Starting at $15,000.</p>

  <svg class="icon" style="left:185px;top:80px" viewBox="0 0 13 13" aria-hidden="true"><g fill="none" stroke="var(--teal)" stroke-width="1"><path d="M1.5 5h2l5-3v9l-5-3h-2z"/><path d="M3.5 8l1 3.5h1.5L5.5 8.3"/><path d="M10 4.5l2-1M10 6.5h2.5M10 8.5l2 1"/></g></svg>
  <p class="v-label" style="left:217px;top:77px">In-verse Advertising</p>
  <p class="v-text" style="left:217px;top:86px">Advertising and promotional opportunities: billboards, "TV", etc.</p>

  <div class="value-word"><div class="value-band"></div><b>VALUE</b></div>
</section>

<!-- Monetization -->
<section class="slide s-money">
  <p class="heading money-title">MONETIZATION</p>
  <p class="money-sign">$</p>
  <p class="money-notes">B2P -&gt; Variable<br>P2C -&gt; 2.5% tx fee<br>B2C -&gt;<br>100% Our Bankroll<br>Consumer to Consumer<br>2.5% Tax on Trans?</p>

  <div class="m-block" style="top:32px"><p class="m-head">In-Game Tax and Microtransactions</p><p class="m-text">A large number of items, upgrades, cosmetics, and more will be made available for purchase. <span>1 - 6.5% Tax/Fee</span> on all transactions.</p></div>
  <div class="m-block" style="top:67px"><p class="m-head">Service Fees</p><p class="m-text">Basic onboarding — One-time fee of $15,000.<br>Over 20 partners.Advanced onboarding — Starting at <span>$100,000.</span></p></div>
  <div class="m-block" style="top:102px"><p class="m-head">Partner Transaction Fees</p><p class="m-text">15% of all transactions made in partner spaces.</p></div>
  <div class="m-block" style="top:123px"><p class="m-head">Extended Service Costs</p><p class="m-text">A la carté services and content creation — Starting at <span>$15,000.</span></p></div>
  <div class="money-bar"></div>
</section>

<!-- Traction -->
<section class="slide s-traction">
  <div class="city" role="img" aria-label="Neon city skyline under a network-lined night sky"></div>
  <p class="traction-copy">&gt;30 prospects in the pipeline, &gt;15 committed and/or paying partners<br>&gt;6,000 members in our Chatterbox community<br>&gt;15 worlds already built, deployed, and playable. Just a few screenshots below:</p>
  <h2 class="heading traction-title">TRACTION</h2>
  <div class="shot" role="img" aria-label="Screenshot of a low-poly island world" style="left:26px;top:59px"><div style="inset:0;background:linear-gradient(160deg,#8fa6a0,#4d6a3c)"></div><i></i></div>
  <div class="shot" role="img" aria-label="Screenshot of a dim red arena" style="left:107px;top:59px"><div style="inset:0;background:linear-gradient(160deg,#6a2a22,#2a0f12)"></div><i></i></div>
  <div class="shot" role="img" aria-label="Screenshot of a neon night club world" style="left:189px;top:59px"><div style="inset:0;background:linear-gradient(160deg,#1a1a3a,#4a1a5a)"></div><i></i></div>
  <div class="shot" role="img" aria-label="Screenshot of a sunset fortress world" style="left:26px;top:111px"><div style="inset:0;background:linear-gradient(160deg,#d0b48a,#3a3a3a)"></div><i></i></div>
  <div class="shot" role="img" aria-label="Screenshot of a forest village world" style="left:107px;top:111px"><div style="inset:0;background:linear-gradient(160deg,#7a8a70,#2a3a22)"></div><i></i></div>
  <div class="shot" role="img" aria-label="Screenshot of a rocky canyon world" style="left:189px;top:111px"><div style="inset:0;background:linear-gradient(160deg,#a89a84,#5a4a3a)"></div><i></i></div>
</section>

<!-- Use of funds -->
<section class="slide s-plan">
  <h2 class="heading plan-title">WHAT WE'RE<br>GOING TO DO</h2>
  <svg class="pie" viewBox="-50 -36 100 80" aria-label="Funding allocation pie chart">
    <defs><linearGradient id="pieSide" x1="0" x2="1"><stop offset="0" stop-color="#12b893"/><stop offset="0.33" stop-color="#12b893"/><stop offset="0.36" stop-color="#5a0c86"/><stop offset="1" stop-color="#5a0c86"/></linearGradient></defs>
    <path d="M-48 0A48 30 0 0 0 48 0L48 12A48 30 0 0 1 -48 12Z" fill="url(#pieSide)"/>
    <path d="M0 0L0 -30A48 30 0 0 1 28.2 -24.3Z" fill="#5b3ab8"/>
    <path d="M0 0L28.2 -24.3A48 30 0 0 1 -14.8 28.5Z" fill="#8a14b8"/>
    <path d="M0 0L-14.8 28.5A48 30 0 0 1 -38.8 -17.6Z" fill="#22f0c0"/>
    <path d="M0 0L-38.8 -17.6A48 30 0 0 1 0 -30Z" fill="#2aa8c8"/>
    <g font-family="Rubik, sans-serif" font-weight="800" font-size="8">
      <text x="-18" y="-17" fill="var(--purple)">15%</text>
      <text x="9" y="-17" fill="var(--teal)">10%</text>
      <text x="-40" y="4" fill="var(--purple)">30%</text>
      <text x="7" y="18" fill="var(--teal)">45%</text>
    </g>
  </svg>
  <div class="plan-band"></div>
  <p class="plan-funding">$2.4MM Total Funding</p>
  <p class="plan-copy">Reach 100% financial independence by deploying the rest of our in-game platform &amp; MaaS toolsets.<br>Expand development team to more rapidly deliver platform roadmap &amp; onboard partners + players.</p>
  <p class="plan-item" style="top:99px"><b>Development 45%</b>Lorem ipsum dolor sit amet stuff, fill this in later or w/e</p>
  <p class="plan-item" style="top:114px"><b>Art Team 30%</b>Lorem ipsum dolor sit amet stuff, fill this in later or w/e</p>
  <p class="plan-item" style="top:129px"><b>Dorian Bank Account 15%</b>Lorem ipsum dolor sit amet stuff, fill this in later or w/e</p>
  <p class="plan-item" style="top:144px"><b>Infrastructure 10%</b>Lorem ipsum dolor sit amet stuff, fill this in later or w/e</p>
</section>

<!-- Closing -->
<section class="slide s-close">
  <p class="close-copy" style="top:67px">Reality is a construct.<br>This is your chance to build it.</p>
  <p class="close-copy" style="top:105px">hello@quintrapex.example</p>
  <div class="socials"><span>Chatterbox</span><span>Chirper</span></div>
</section>

</body>
</html>
```